Kelvaro Pools

Luxury pool designer builder brochure

Company name is "Kelvaro"
Tag line is "Pools for the Mind Body & Soul"
Maybe integrate "Luxury Urban Lifestyle"

Target Market(s)

30 to 65 income of 200000.00 plus Affluent, high end life style
Luxury living

Industry/Entity Type

It Company

Font styles to use
Serif

Colors
000000

Requirements
Must have
• NOTE:
• Please remove the "Aquatic environments for the under the logo.
• I want a black background with a very contemporary feel.
• This is a luxury lifestyle product.

```html
<!DOCTYPE html>
<html lang="en">
<head>
<meta charset="utf-8">
<title>Kelvaro Pools — Brochure Cover</title>
<link rel="stylesheet" href="https://fonts.googleapis.com/css2?family=Bodoni+Moda:ital,opsz,wght@0,6..96,400;0,6..96,500&display=swap">
<style>
  :root {
    --sheet: #000000;
    --ink: #ffffff;
    --ink-muted: #bdbdbd;
  }
  * { margin: 0; padding: 0; box-sizing: border-box; }
  html, body {
    width: 1200px;
    height: 800px;
    overflow: hidden;
    background: var(--sheet);
  }
  .brochure {
    position: relative;
    width: 1200px;
    height: 800px;
    background: var(--sheet);
    font-family: "Bodoni Moda", "Didot", serif;
    color: var(--ink);
    -webkit-font-smoothing: antialiased;
  }
  .tagline {
    position: absolute;
    top: 168px;
    right: 96px;
    text-align: right;
    font-size: 34px;
    font-weight: 400;
    font-optical-sizing: auto;
    line-height: 1.12;
    letter-spacing: -0.005em;
  }
  .brand {
    position: absolute;
    right: 96px;
    bottom: 150px;
    font-size: 20px;
    font-weight: 500;
    letter-spacing: 0.22em;
    text-transform: none;
    line-height: 1;
  }
  .address {
    position: absolute;
    left: 0;
    right: 0;
    bottom: 62px;
    text-align: center;
    font-size: 12px;
    letter-spacing: 0.18em;
    color: var(--ink-muted);
  }
</style>
</head>
<body>
  <main class="brochure">
    <h1 class="tagline">Pools for the Mind<br>Body &amp; Soul</h1>
    <p class="brand">Kelvaro</p>
    <p class="address">address</p>
  </main>
</body>
</html>
```